Business card-Tales From The Harbor Gate

Looking for a business card. I have a website I designed "TalesFromTheHarborGate.com I am not a graphic artist and may at some point need help with my website too. Used the font "Hello Stockholm" on my website. I am a writer, looking to get published. Liked the "feel" of the cover below. No cliche typwriters, keyboards, pens. - Edgar P. Lindqvist
Updates

Not 100% sold on needing the owls, just a place to begin. I probably sounds like I'm going to be a pain to work with, I was a video production manager for 15+ years. When I would give an editor or graphic artist a project and let them run with it, the results were typically beyond my expectations. I give the idea then as the artists touch it, and adds value I could never bring to the project. Make something you would be proud of, don't try to second-guess me.

Target Market(s)

Agents, publishers, people I want to buy my book once I get it published

Industry/Entity Type

Publishing

Contact Information for Business Card

Edgar P. Lindqvist
TalesFromTheHarborGate.com
Phone #-TBD
Edgar@TalesFromTheHarbroGate.com
Maybe address; 418 N. 7th St Alder Falls, MT 82947

Colors
fcca95
3277b5

Requirements
Must have
• I like the "chromatic" feel of the attached cover. As you can see from my website, I'm an owl fan. Those pictures I took and do own the rights too. Not sure if they are approritae for a business card.
Should not have
• Cliche I like the "chromatic" feel of the attached book cover.
• I will need help with my website at some point too. I want the website to be easy for me to update, and reflect the same feel as the card. I write adventure, mystery. I have romance in my books too...Adventure of Romance, Romance of adventure, I am not sure but those words were like by an author firned of mine. They are rather "light" reading too.

```html
<!DOCTYPE html>
<html lang="en">
<head>
<meta charset="utf-8">
<title>Edgar P. Lindqvist — Business Card</title>
<link rel="stylesheet" href="https://fonts.googleapis.com/css2?family=Open+Sans:wght@400;600;700&family=Great+Vibes&display=swap">
<style>
  :root {
    --harbor-blue: #1c71b6;
    --sand: #f1c68a;
    --mist: #e3e4e5;
    --paper: #ffffff;
    --ink: #2f3033;
    --backdrop: #ece9e4;
  }
  * { box-sizing: border-box; margin: 0; padding: 0; }
  html, body {
    width: 1200px;
    height: 800px;
    overflow: hidden;
    background: var(--backdrop);
  }
  .stage {
    position: relative;
    width: 1200px;
    height: 800px;
    display: flex;
    align-items: center;
    justify-content: center;
    gap: 60px;
  }
  .card {
    position: relative;
    width: 520px;
    height: 300px;
    box-shadow: 0 6px 18px rgba(0, 0, 0, 0.12);
    overflow: hidden;
  }

  /* Back: contact side */
  .card-back {
    background: var(--harbor-blue);
    color: var(--paper);
  }
  .signature {
    position: absolute;
    left: 92px;
    top: 150px;
    transform: translate(-50%, -50%) rotate(-90deg);
    font-family: "Great Vibes", cursive;
    font-size: 66px;
    line-height: 1;
    white-space: nowrap;
    color: var(--paper);
  }
  .divider {
    position: absolute;
    left: 180px;
    top: 34px;
    width: 2px;
    height: 232px;
    background: var(--paper);
  }
  .contact-list {
    position: absolute;
    left: 206px;
    top: 52px;
    list-style: none;
    font-family: "Open Sans", sans-serif;
    font-size: 14.5px;
    line-height: 1;
    white-space: nowrap;
  }
  .contact-list li + li { margin-top: 42px; }

  /* Front: name side */
  .card-front {
    background: var(--paper);
    padding: 16px;
  }
  .front-panel {
    position: relative;
    width: 100%;
    height: 100%;
    background: var(--mist);
  }
  .front-shapes {
    position: absolute;
    inset: 0;
    display: block;
  }
  .identity {
    position: absolute;
    inset: 0;
    display: flex;
    flex-direction: column;
    align-items: center;
    justify-content: center;
    font-family: "Open Sans", sans-serif;
    color: var(--ink);
  }
  .identity-name {
    font-size: 27px;
    font-weight: 700;
    letter-spacing: 0.2px;
  }
  .identity-role {
    margin-top: 4px;
    font-size: 13px;
    font-weight: 600;
    letter-spacing: 2.5px;
  }
</style>
</head>
<body>
  <main class="stage">
    <section class="card card-back" aria-label="Business card, contact side">
      <div class="signature">Lindqvist</div>
      <div class="divider"></div>
      <ul class="contact-list">
        <li>WWW.TalesFromTheHarborGate.com</li>
        <li>555-010-274</li>
        <li>Edgar@TalesFromTheHarborGate.com</li>
        <li>418 N. 7th St, Alder Falls, MT 82947</li>
      </ul>
    </section>

    <section class="card card-front" aria-label="Business card, name side">
      <div class="front-panel">
        <svg class="front-shapes" viewBox="0 0 488 268" preserveAspectRatio="none" aria-hidden="true">
          <polygon points="0,0 135,0 0,262" fill="var(--harbor-blue)"/>
          <polygon points="135,0 222,0 96,76" fill="var(--sand)"/>
          <polygon points="488,268 353,268 488,6" fill="var(--harbor-blue)"/>
          <polygon points="353,268 266,268 392,192" fill="var(--sand)"/>
        </svg>
        <div class="identity">
          <h1 class="identity-name">Edgar P. Lindqvist</h1>
          <p class="identity-role">WRITER</p>
        </div>
      </div>
    </section>
  </main>
</body>
</html>
```